Two sided business card template for:

Nook 4 Keeps Storage
1873 Brindle Avenue,
Saskatoon, SK
S4R 2M6
306-517-3482
www.nook4keeps.ca

Front side should be standard business card information. Sample should be for Darren Kowalchuk, Operations Manager, darren@nook4keeps.ca

Back side should be an advertisement for the storage facility. Some points about our facility are below you may use some or all of these features in the ad.

-Online payments and bookings
-Seasonal bicycle, tire, and motorcycle storage
-24hr self storage access
-Safe, and secure, with digital video surveillance
-Airport location

Card could have, but doesn't need a clever tag line containing the company name

Finished design must be in Microsoft word, or publisher format, and text must be editable.

```html
<!DOCTYPE html>
<html lang="en">
<head>
<meta charset="utf-8">
<title>Nook 4 Keeps Storage – Business Card</title>
<link rel="stylesheet" href="https://fonts.googleapis.com/css2?family=Open+Sans:wght@400;600;700&display=swap">
<style>
  :root {
    --backdrop: #222326;
    --card-white: #ffffff;
    --ink: #1c1c1c;
    --brand-blue: #1a6fc0;
    --brand-blue-light: #3d8fdc;
    --brand-red: #d8262d;
    --stripe: #ffffff;
  }
  * { box-sizing: border-box; margin: 0; padding: 0; }
  html, body {
    width: 1200px; height: 800px; overflow: hidden;
    background: var(--backdrop);
    font-family: "Open Sans", Arial, sans-serif;
  }
  .canvas { position: relative; width: 1200px; height: 800px; }

  .card {
    position: absolute;
    width: 540px; height: 309px;
    overflow: hidden;
    box-shadow: 0 10px 24px rgba(0,0,0,0.45);
  }

  /* Back side – advertisement */
  .card-back { left: 50px; top: 110px; background: var(--card-white); }
  .brand-frame {
    position: absolute; left: 0; top: 92px;
    width: 250px; height: 136px;
    border: 2px solid var(--ink);
    display: flex; align-items: center; justify-content: center; gap: 10px;
  }
  .feature-list {
    position: absolute; left: 272px; top: 100px;
    list-style: none;
    font-size: 12.5px; line-height: 1.35; color: var(--ink);
  }

  /* Shared brand name */
  .brand-mark { width: 20px; height: 20px; background: var(--brand-red); flex: none; }
  .brand-name {
    font-weight: 700; font-size: 17px; line-height: 1.1;
    color: var(--brand-red); text-align: center; letter-spacing: 0.5px;
  }

  /* Front side – contact card */
  .card-front {
    left: 610px; top: 380px;
    background: linear-gradient(160deg, var(--brand-blue-light) 0%, var(--brand-blue) 55%, #1662ad 100%);
    color: #ffffff;
  }
  .stripes { position: absolute; inset: 0; }
  .brand-panel {
    position: absolute; left: 32px; top: 44px;
    width: 178px; height: 104px;
    background: var(--card-white);
    display: flex; align-items: center; justify-content: center; gap: 8px;
  }
  .brand-panel .brand-name { font-size: 15px; }
  .holder { position: absolute; left: 312px; top: 40px; }
  .holder-name { font-size: 16px; font-weight: 400; }
  .holder-role { font-size: 11px; color: var(--brand-red); margin-top: 1px; }
  .address {
    position: absolute; left: 286px; top: 196px;
    font-size: 11px; line-height: 1.75; font-style: normal;
  }
  .contact {
    position: absolute; left: 32px; top: 216px;
    font-size: 12px; line-height: 1.9;
  }
</style>
</head>
<body>
<main class="canvas">

  <section class="card card-back" aria-label="Card back: advertisement">
    <div class="brand-frame">
      <span class="brand-mark"></span>
      <span class="brand-name">NOOK 4 KEEPS<br>STORAGE</span>
    </div>
    <ul class="feature-list">
      <li>Airport location</li>
      <li>24hr self storage access</li>
      <li>Online payments and bookings</li>
      <li>Seasonal bicycle, tire, and motorcycle storage</li>
      <li>Safe, and secure, with digital video surveillance</li>
    </ul>
  </section>

  <section class="card card-front" aria-label="Card front: contact details">
    <svg class="stripes" width="540" height="309" viewBox="0 0 540 309" aria-hidden="true">
      <g stroke="var(--stripe)" stroke-width="3.5">
        <line x1="0" y1="160" x2="540" y2="160"/>
        <line x1="0" y1="174" x2="540" y2="174"/>
        <line x1="0" y1="188" x2="540" y2="188"/>
        <line x1="228" y1="0" x2="228" y2="309"/>
        <line x1="242" y1="0" x2="242" y2="309"/>
        <line x1="256" y1="0" x2="256" y2="309"/>
      </g>
    </svg>

    <div class="brand-panel">
      <span class="brand-mark"></span>
      <span class="brand-name">NOOK 4 KEEPS<br>STORAGE</span>
    </div>

    <div class="holder">
      <p class="holder-name">Darren Kowalchuk</p>
      <p class="holder-role">Operations Manager</p>
    </div>

    <address class="address">
      Nook 4 Keeps Storage<br>
      1873 Brindle Avenue,<br>
      Saskatoon, SK<br>
      S4R 2M6
    </address>

    <div class="contact">
      <p>306-517-3482</p>
      <p>www.nook4keeps.ca</p>
      <p>darren@nook4keeps.ca</p>
    </div>
  </section>

</main>
</body>
</html>
```